Facebook Page Design for a Medical Billing Business

We need help designing a facebook page that is professional, yet friendly that will attract medical practitioners (doctors, therapists, nutritionists, chiropractors, etc) to check out and follow our business. I have attached our logo which must be incorporated in the design.

```html
<!DOCTYPE html>
<html lang="en">
<head>
<meta charset="utf-8">
<title>Velix Medical Billing — Page Cover</title>
<link rel="stylesheet" href="https://fonts.googleapis.com/css2?family=Cinzel:wght@400;500&display=swap">
<style>
  :root {
    --bg: #000000;
    --brand: #a468c8;
    --text: #ffffff;
    --icon: #d462a6;
    --band-start: #6a5bb8;
    --band-end: #d765a8;
  }
  * { box-sizing: border-box; margin: 0; padding: 0; }
  html, body {
    width: 1200px;
    height: 462px;
    overflow: hidden;
    background: var(--bg);
  }
  .cover {
    position: relative;
    width: 1200px;
    height: 462px;
    background: var(--bg);
    font-family: "Cinzel", "Times New Roman", serif;
  }
  .brand-name {
    position: absolute;
    left: 270px;
    top: 128px;
    width: 620px;
    display: flex;
    flex-direction: column;
    align-items: center;
    color: var(--brand);
    font-weight: 400;
    line-height: 1;
  }
  .brand-name__word {
    display: block;
    font-size: 160px;
    letter-spacing: 4px;
  }
  .brand-name__tagline {
    display: flex;
    align-items: center;
    gap: 14px;
    width: 590px;
    margin-top: 6px;
    font-size: 23px;
    letter-spacing: 5px;
    white-space: nowrap;
  }
  .brand-name__tagline::before,
  .brand-name__tagline::after {
    content: "";
    flex: 1;
    height: 2px;
    background: var(--brand);
  }
  .contact-bar {
    position: absolute;
    left: 0;
    right: 0;
    top: 396px;
    display: flex;
    justify-content: center;
    align-items: center;
    gap: 14px;
    color: var(--text);
    font-size: 23px;
    font-weight: 500;
    font-style: normal;
  }
  .contact-bar__item {
    display: flex;
    align-items: center;
    gap: 10px;
  }
  .contact-bar__icon {
    width: 20px;
    height: 20px;
    flex: none;
  }
  .contact-bar__divider {
    width: 1px;
    height: 24px;
    background: var(--text);
  }
  .footer-band {
    position: absolute;
    left: 0;
    right: 0;
    bottom: 0;
    height: 25px;
    background: linear-gradient(90deg, var(--band-start), var(--band-end));
  }
</style>
</head>
<body>
<main class="cover">
  <h1 class="brand-name">
    <span class="brand-name__word">VELIX</span>
    <span class="brand-name__tagline">MEDICAL BILLING</span>
  </h1>

  <address class="contact-bar">
    <span class="contact-bar__item">
      <svg class="contact-bar__icon" viewBox="0 0 20 20" aria-hidden="true">
        <rect x="1" y="4" width="18" height="12" rx="1" fill="var(--icon)"/>
        <path d="M1.5 4.5 L10 11 L18.5 4.5" fill="none" stroke="var(--bg)" stroke-width="1.5"/>
      </svg>
      Admin@velix.example
    </span>
    <span class="contact-bar__divider"></span>
    <span class="contact-bar__item">
      <svg class="contact-bar__icon" viewBox="0 0 20 20" aria-hidden="true" fill="none" stroke="var(--icon)" stroke-width="1.5">
        <circle cx="10" cy="10" r="8.5"/>
        <ellipse cx="10" cy="10" rx="3.8" ry="8.5"/>
        <line x1="1.5" y1="10" x2="18.5" y2="10"/>
        <path d="M3 5.5 H17 M3 14.5 H17"/>
      </svg>
      www.velix.example
    </span>
    <span class="contact-bar__divider"></span>
    <span class="contact-bar__item">
      <svg class="contact-bar__icon" viewBox="0 0 20 20" aria-hidden="true">
        <path d="M5.2 1.8 L7.6 5.6 L6 7.4 C7 9.8 10.2 13 12.6 14 L14.4 12.4 L18.2 14.8 L16.6 18 C9.6 18.2 1.8 10.4 2 3.4 Z" fill="var(--icon)"/>
      </svg>
      425-555-0187
    </span>
  </address>

  <div class="footer-band"></div>
</main>
</body>
</html>
```